Community Harvest Festival Poster

Seeking a poster design to advertise our community’s annual Harvest Festival. We will utilize and display printed posters as well as distribute PDFs via our weekly e-news letters. This years "theme" is, "Copper Lantern/Maple Ridge Fair, Where City and Country Meet." The vibe is a bohemian, beatnik, street scene, meets a old fashioned orchard.

Target Market(s)

NYC School Community- should appeal to an audience that ranges from kids to grandparents. Very family oriented, with wide appeal, and must be eye catching.

Other font styles liked:
• One style should be more of a "Country" font, the other should have more of a clean city vibe.

Colors
acd037
ffc214
f68e4e
eaf2ce

Requirements
Must have
• The following copy:
• Copper Lantern Maple Ridge Fair
• Where City and Country Meet
• Celebrate C&C With Great Food, Music, Entertainment, And Fun!
• Saturday, October 19th 2019
• 12:00-4:00pm
• Tickets will be available for sale at Drop off and Pick up
Nice to have
• I'm not limited, but a couple of ideas that could be cool:
• One incorporated the background of a street, i.e. pavement, which has leaves blowing over it, and perhaps an apple or two rolling onto the page.
• Another has a diagonal breakup of the image, with one side pavement and the other side rustic wood, also with leaves sweeping across.
• I've also attached images of previous festival posters that I have gravitated to for some idea of quality I'm looking for.
Should not have
• Anything inappropriate for children.

```html
<!DOCTYPE html>
<html lang="en">
<head>
<meta charset="utf-8">
<title>Copper Lantern Maple Ridge Fair – Harvest Festival Poster</title>
<link rel="stylesheet" href="https://fonts.googleapis.com/css2?family=Dancing+Script:wght@700&family=Kaushan+Script&family=Montserrat:wght@500;700&display=block">
<style>
  :root {
    --stage: #ecebe8;
    --paper: #ffffff;
    --gold: #ffc214;
    --green: #8dbb1e;
    --green-bright: #acd037;
    --rust: #b8430f;
    --ink: #1a1a1a;
    --leaf-orange: #f68e4e;
    --leaf-amber: #f7a21b;
    --leaf-red: #c93a12;
    --leaf-pale: #fbe3c4;
  }
  * { box-sizing: border-box; margin: 0; padding: 0; }
  html, body { width: 1200px; height: 1200px; overflow: hidden; }
  body { background: var(--stage); position: relative; }

  .poster {
    position: absolute;
    left: 205px; top: 35px;
    width: 790px; height: 1130px;
    background: var(--paper);
    overflow: hidden;
  }

  .art { position: absolute; }
  .art--corner-leaves {
    right: 0; top: 0; width: 300px; height: 330px;
    background: radial-gradient(circle at 85% 15%, var(--leaf-orange), var(--leaf-amber) 45%, rgba(247,162,27,0.35) 70%, rgba(255,255,255,0) 78%);
  }
  .art--drifting-leaves {
    left: 100px; top: 60px; width: 260px; height: 150px;
    background: radial-gradient(ellipse at 50% 50%, var(--leaf-pale), rgba(251,227,196,0) 70%);
  }
  .art--leaf-border {
    left: 0; bottom: 0; width: 100%; height: 420px;
    background: linear-gradient(to bottom, rgba(247,162,27,0) 0%, rgba(247,162,27,0.55) 22%, var(--leaf-amber) 40%, var(--leaf-orange) 65%, var(--leaf-red) 100%);
  }

  .title-frame {
    position: absolute;
    left: 140px; top: 240px;
    width: 560px; height: 245px;
  }
  .title-frame svg { position: absolute; inset: 0; }
  .title {
    position: absolute; inset: 0;
    padding: 0 24px;
    display: flex; flex-direction: column; align-items: center; justify-content: center;
    font-family: "Dancing Script", cursive;
    font-weight: 700;
    line-height: 1.1;
    white-space: nowrap;
  }
  .title__line--top { color: var(--gold); font-size: 70px; margin-left: 30px; }
  .title__line--bottom { color: var(--green); font-size: 70px; }

  .tagline {
    position: absolute; left: 0; right: 0; top: 510px;
    text-align: center;
    font-family: "Montserrat", sans-serif; font-weight: 700;
    font-size: 39px; color: var(--gold);
  }
  .subline {
    position: absolute; left: 0; right: 0; top: 570px;
    text-align: center;
    font-family: "Montserrat", sans-serif; font-weight: 500;
    font-size: 18px; color: var(--ink);
  }
  .date-band {
    position: absolute; left: 80px; width: 640px; top: 610px; height: 54px;
    border-radius: 27px;
    background: var(--green);
    display: flex; align-items: center; justify-content: center; gap: 22px;
    font-family: "Montserrat", sans-serif; font-weight: 700;
    font-size: 25px; color: #fff;
  }
  .date-band__divider { font-weight: 500; }
  .tickets {
    position: absolute; left: 0; right: 0; top: 680px;
    text-align: center;
    font-family: "Kaushan Script", cursive;
    font-size: 29px; color: var(--ink);
  }
</style>
</head>
<body>
  <main class="poster">
    <div class="art art--drifting-leaves" role="img" aria-label="Pale maple leaves drifting across the top of the poster"></div>
    <div class="art art--corner-leaves" role="img" aria-label="Cluster of orange, yellow and red autumn maple leaves in the top right corner"></div>
    <div class="art art--leaf-border" role="img" aria-label="Border of layered autumn maple leaves, red berries and a rust-coloured leafy sprig along the bottom"></div>

    <section class="title-frame">
      <svg width="560" height="245" viewBox="0 0 560 245" aria-hidden="true">
        <polyline points="470,3 557,3 557,242 3,242 3,3 400,3" fill="none" stroke="var(--rust)" stroke-width="4"/>
      </svg>
      <h1 class="title">
        <span class="title__line--top">Copper Lantern</span>
        <span class="title__line--bottom">Maple Ridge Fair</span>
      </h1>
    </section>

    <p class="tagline">Where City and Country Meet</p>
    <p class="subline">Celebrate C&amp;C With Great Food, Music, Entertainment, And Fun!</p>
    <p class="date-band">
      <span>Saturday, October 19th 2019</span>
      <span class="date-band__divider">|</span>
      <span>12:00-4:00pm</span>
    </p>
    <p class="tickets">Tickets will be available for sale at Drop off and Pick up</p>
  </main>
</body>
</html>
```